International Educational/Tuition/Learning Center

Company Background:
- Business card for a educational/tuition/learning center that provides supplementary lessons for students in Grade 7 to 12 ( Secondary and JC syllabus in the GCE 'O' and GCE 'A' level context but not limited to these. Future plans will be to cater for SAT, IB and HSCs programs.
- Name of company is called "THE QUILL AND LANTERN".
- Vision is to complement the basic principles of the rote learning culture and value-add by training the students to think out of the box and preserve creativity.
- To re-define and retain the value of the learning process.

Sketch Design:
- Simple and classy design that is mainly white-based with tinge of refreshing bright lime green.
- "New Age" simple and classy design that appeals to teenagers and young adults.
- Logo design to reinforce the vision of company.

Rough idea of what we have in mind but pls do not let this restrict your creativity:
- White and bright green base
- 2 sided print
- Front with simple information of Name and Designation as well as de-bossed/letterpressed print
- Details of on reverse side
- Contact details can be categorized as " find me" - address, "call me" - contact number , "email me" - email address, " Find out more"- website.

Information:

Name: Derek M Thalwin
Title: Managing Director
Address: 41 Kestrel Lane, #07-15, Singapore 654321
Contact: +65 93417260
Email: derekthalwin@mailvexo.com
Website: www.qnl-study.com

Thank you all in advance! Looking forward to some amazing designs from all you talented folks!
Updates

hi all,

have updated the projected to a guranteed status from the initial refundable status.

Thanks 

Dear designers,

I've included more info into the brief on design elements to include. 

Thanks for your participation and efforts!

Cheers!

Target Market(s)

young parents with school going children

Industry/Entity Type

Training

Requirements
Must have
• debossed/letterpressed logo
feel free to be creative with ur designs!
Nice to have
• round edges
Logo/name could have some elements of education/knowledge/path-to-learning incorporated in the design concept

```html
<!DOCTYPE html>
<html lang="en">
<head>
<meta charset="utf-8">
<title>The Quill and Lantern – Business Card</title>
<link rel="stylesheet" href="https://fonts.googleapis.com/css2?family=Montserrat:wght@600;700&family=Questrial&display=swap">
<style>
  :root {
    --lime: #66b32e;
    --lime-soft: #a9d489;
    --lime-pale: #dcedcf;
    --paper: #f5f5f4;
    --edge: #141414;
    --ink: #1e1e1e;
    --backdrop: #e8e5df;
  }
  * { box-sizing: border-box; margin: 0; padding: 0; }
  html, body {
    width: 1200px;
    height: 900px;
    overflow: hidden;
    background: var(--backdrop);
  }
  .canvas {
    position: relative;
    width: 1200px;
    height: 900px;
  }
  .card {
    position: absolute;
    width: 930px;
    height: 420px;
    border: 6px solid var(--edge);
    border-radius: 26px;
    overflow: hidden;
  }

  /* Front side */
  .card--front {
    left: 45px;
    top: 18px;
    background: var(--lime);
  }
  .card--front .brand-name {
    position: absolute;
    left: 140px;
    top: 96px;
    font-family: "Montserrat", sans-serif;
    font-weight: 700;
    font-size: 50px;
    letter-spacing: 0.5px;
    color: var(--paper);
    white-space: nowrap;
  }
  .icon-art {
    position: absolute;
    background: linear-gradient(135deg, var(--paper) 0%, var(--paper) 35%, var(--lime-pale) 100%);
    border: 3px solid var(--paper);
  }
  .icon-art--hourglass { left: 18px;  top: 252px; width: 56px;  height: 46px; }
  .icon-art--books     { left: 88px;  top: 236px; width: 78px;  height: 62px; }
  .icon-art--notes     { left: 180px; top: 222px; width: 120px; height: 76px; }
  .icon-art--globe     { left: 326px; top: 188px; width: 246px; height: 110px; }
  .icon-art--board     { left: 628px; top: 176px; width: 300px; height: 122px; }

  /* Back side */
  .card--back {
    left: 190px;
    top: 458px;
    background: var(--paper);
  }
  .card--back .band {
    position: absolute;
    left: 0; top: 0;
    width: 100%;
    height: 134px;
    background: var(--lime);
    display: flex;
    align-items: center;
    justify-content: center;
  }
  .card--back .brand-name {
    font-family: "Montserrat", sans-serif;
    font-weight: 700;
    font-size: 44px;
    letter-spacing: 0.5px;
    color: var(--paper);
    white-space: nowrap;
    margin-top: 4px;
  }
  .path-art {
    position: absolute;
    left: 748px;
    top: 134px;
    width: 88px;
    height: 274px;
    background: linear-gradient(180deg, var(--lime-pale) 0%, var(--lime-soft) 45%, var(--lime) 100%);
  }
  .details {
    position: absolute;
    left: 34px;
    top: 244px;
    font-family: "Questrial", sans-serif;
    font-size: 20px;
    line-height: 25px;
    color: var(--ink);
    list-style: none;
  }
  .details .label {
    font-family: "Montserrat", sans-serif;
    font-weight: 700;
    font-size: 18px;
    color: var(--lime);
    margin-right: 4px;
  }
  .details .role {
    font-family: "Montserrat", sans-serif;
    font-weight: 700;
    font-size: 18px;
    color: var(--lime);
  }
</style>
</head>
<body>
<main class="canvas">

  <section class="card card--front" aria-label="Card front">
    <p class="brand-name">THE QUILL AND LANTERN</p>
    <div class="icon-art icon-art--hourglass" role="img" aria-label="Hourglass illustration"></div>
    <div class="icon-art icon-art--books" role="img" aria-label="Row of books illustration"></div>
    <div class="icon-art icon-art--notes" role="img" aria-label="Notes and pencil illustration"></div>
    <div class="icon-art icon-art--globe" role="img" aria-label="Globe with magnifying glass illustration"></div>
    <div class="icon-art icon-art--board" role="img" aria-label="Chalkboard with equation illustration"></div>
  </section>

  <section class="card card--back" aria-label="Card back">
    <div class="band">
      <p class="brand-name">THE QUILL AND LANTERN</p>
    </div>
    <div class="path-art" role="img" aria-label="Illustration of a path leading into the distance"></div>
    <ul class="details">
      <li>Derek M Thalwin</li>
      <li class="role">Managing Director</li>
      <li><span class="label">Address:</span>41 Kestrel Lane, #07-15, Singapore 654321</li>
      <li><span class="label">Contact:</span> +65 93417260</li>
      <li><span class="label">Email:</span>derekthalwin@mailvexo.com</li>
      <li><span class="label">Website:</span>www.qnl-study.com</li>
    </ul>
  </section>

</main>
</body>
</html>
```